Harbor Key Realty - New Agent Opportunity Overview

We want to create a one (1) page brochure to highlight what Harbor Key Realty (a real estate brokerage) offers new agents. I have uploaded a Word doc that has all the text we want on the flyer. We want a professional looking design.
Industry/Entity Type
Real Estate Agent
Colors
3176b5
33a6d7

```html
<!DOCTYPE html>
<html lang="en">
<head>
<meta charset="utf-8">
<title>Harbor Key Realty – New Agent Opportunity</title>
<link rel="stylesheet" href="https://fonts.googleapis.com/css2?family=Bebas+Neue&family=Roboto:wght@400;500;700&family=Montserrat:wght@600&display=swap">
<style>
:root{
  --brand-blue:#3176b5;
  --accent-blue:#33a6d7;
  --ink:#2d2d2d;
  --text:#333;
  --panel-grey:#e3e3e5;
  --row-light:#dadada;
  --row-dark:#c6c6c6;
  --white:#fff;
}
*{margin:0;padding:0;box-sizing:border-box}
html,body{width:900px;height:1200px;overflow:hidden;background:#fff}
.flyer{position:relative;width:900px;height:1200px;background:var(--white);font-family:'Roboto',Arial,sans-serif;color:var(--text)}
.hero-shapes{position:absolute;left:0;top:0}
.brand-mark{position:absolute;left:54px;top:56px;display:flex;align-items:center;gap:12px;font-family:'Montserrat',sans-serif;font-weight:600;font-size:22px;letter-spacing:3px;color:var(--ink);text-transform:uppercase}
.brand-mark .mark-square{width:20px;height:20px;background:var(--brand-blue)}
.hero-title{position:absolute;left:54px;top:156px;font-family:'Bebas Neue',sans-serif;font-weight:400;font-size:78px;line-height:70px;color:var(--white);text-transform:uppercase;letter-spacing:0.5px}
.hero-rule{position:absolute;left:54px;top:306px;width:135px;height:4px;background:var(--white)}
.hero-sub{position:absolute;left:54px;top:330px;font-weight:700;font-size:24px;line-height:30px;color:var(--white)}
.tab{position:absolute;top:452px;height:50px;display:flex;align-items:center;justify-content:center;color:var(--white);font-weight:500;font-size:23px;border-radius:6px}
.tab--blue{left:51px;width:403px;background:var(--brand-blue)}
.tab--dark{left:457px;width:390px;background:var(--ink)}
.column{position:absolute;top:534px}
.column--left{left:51px;width:330px}
.column--right{left:457px;width:400px}
.col-heading{font-weight:500;font-size:20px;color:var(--brand-blue);padding-bottom:4px;position:relative}
.col-heading::after{content:"";position:absolute;left:0;bottom:-4px;width:120px;height:2px;background:#999}
.checklist{list-style:none;margin-top:22px}
.checklist li{position:relative;padding-left:22px;font-size:13.5px;line-height:29.5px;color:var(--text)}
.checklist li::before{content:"";position:absolute;left:0;top:10px;width:10px;height:10px;border:1.5px solid var(--brand-blue);border-radius:1px}
.checklist li::after{content:"";position:absolute;left:3px;top:10px;width:4px;height:7px;border:solid var(--brand-blue);border-width:0 2px 2px 0;transform:rotate(40deg)}
.col-divider{position:absolute;left:400px;top:534px;width:2px;height:295px;background:#666}
.split-table{position:absolute;left:457px;top:687px;width:390px;border-collapse:collapse;font-size:12.5px}
.split-table th{background:var(--brand-blue);color:var(--white);font-weight:700;text-align:left;height:32px;padding-left:18px;font-size:14px}
.split-table th+th,.split-table td+td{border-left:2px solid var(--white)}
.split-table td{height:28px;padding-left:18px;color:#444}
.split-table tr:nth-child(odd) td{background:var(--row-light)}
.split-table tr:nth-child(even) td{background:var(--row-dark)}
.perks-panel{position:absolute;left:51px;top:869px;width:796px;height:225px;background:var(--panel-grey)}
.perks-ribbon{position:absolute;left:279px;top:858px}
.perks-ribbon span{position:absolute;left:0;top:0;width:343px;height:47px;display:flex;align-items:center;justify-content:center;color:var(--white);font-weight:500;font-size:21px}
.perks-list{position:absolute;top:942px}
.perks-list--left{left:86px}
.perks-list--right{left:514px}
.perks-list .checklist{margin-top:0}
.perks-divider{position:absolute;left:440px;top:930px;height:145px;border-left:2px dashed #777}
.footer{position:absolute;left:0;top:1122px;width:900px;height:78px;background:var(--ink);display:flex;align-items:center;justify-content:center;color:var(--white);font-weight:500;font-size:25px;letter-spacing:2px}
</style>
</head>
<body>
<main class="flyer">
  <svg class="hero-shapes" width="900" height="440" viewBox="0 0 900 440">
    <defs>
      <linearGradient id="houseTone" x1="0" y1="0" x2="0" y2="1">
        <stop offset="0" stop-color="#5a86c4"/>
        <stop offset="0.45" stop-color="#b9c6cf"/>
        <stop offset="0.75" stop-color="#8f9a8a"/>
        <stop offset="1" stop-color="#4a5560"/>
      </linearGradient>
    </defs>
    <polygon points="0,133 410,133 550,423 0,423" fill="#3176b5"/>
    <polygon points="514,0 900,0 900,423 550,423 382,188" fill="url(#houseTone)" role="img" aria-label="Photo of a large two-storey luxury home with arched windows and a paved driveway"/>
    <rect x="0" y="423" width="900" height="11" fill="#2d2d2d"/>
  </svg>

  <div class="brand-mark"><span class="mark-square"></span>Harbor Key Realty</div>

  <h1 class="hero-title">Harbor Key<br>Realty</h1>
  <div class="hero-rule"></div>
  <p class="hero-sub">HKR Home Center Quillmere,<br>Eastvale is Now Open!</p>

  <div class="tab tab--blue">Ignite your Real Estate Business</div>
  <div class="tab tab--dark">Join Harbor Key Realty</div>

  <section class="column column--left">
    <h2 class="col-heading">Consumer Direct Advantage</h2>
    <ul class="checklist">
      <li>Lender Referrals</li>
      <li>Nestquarry Leads</li>
      <li>Shared Lender Leads</li>
      <li>Listhaven.com / NearbyNestHomes.com</li>
      <li>Credit Trigger Campaigns</li>
      <li>Consumer Behavior Campaigns</li>
      <li>HKR Call Center Marketing Team</li>
      <li>HKR Sponsored Local Events</li>
    </ul>
  </section>

  <div class="col-divider"></div>

  <section class="column column--right">
    <h2 class="col-heading">Maximized Compensation</h2>
    <ul class="checklist">
      <li>No desk fees. No royalty fees. No franchise fees.</li>
      <li>Company paid E&amp;O</li>
      <li>Transaction fee of $550 includes Transaction Coordinator</li>
    </ul>
  </section>

  <table class="split-table">
    <thead><tr><th>Type of Deal</th><th>Commission Split</th></tr></thead>
    <tbody>
      <tr><td>Self-Generated</td><td>90% /10%</td></tr>
      <tr><td>Lender Referred Leads</td><td>70% /30%</td></tr>
      <tr><td>HKR Generated Leads / Referrals</td><td>55% /45%</td></tr>
    </tbody>
  </table>

  <div class="perks-panel"></div>
  <div class="perks-ribbon">
    <svg width="343" height="47" viewBox="0 0 343 47">
      <polygon points="0,0 343,0 330,47 13,47" fill="#3176b5"/>
    </svg>
    <span>Consumer Direct Advantage</span>
  </div>

  <div class="perks-list perks-list--left">
    <ul class="checklist">
      <li>Powerful Suite of Cloud Based Tools</li>
      <li>IDX, CRM and Transaction Management</li>
      <li>HKR Call Center Support for Leads and Deals</li>
      <li>Transaction Coordinator</li>
      <li>Virtual Assistants Available</li>
    </ul>
  </div>
  <div class="perks-divider"></div>
  <div class="perks-list perks-list--right">
    <ul class="checklist">
      <li>24/7 Workspace Access</li>
      <li>Coaching / Mentoring</li>
      <li>Social Media / Marketing Expertise</li>
      <li>Nationwide Partnerships with Top Lenders</li>
    </ul>
  </div>

  <footer class="footer">www.harborkeyrealty.com</footer>
</main>
</body>
</html>
```